I need a new design for my real estate signage!

Would like a new design for my real estate signs. I do have a logo that needs to be used along with the word AVAILABLE and my phone number 505-281-7094

Target Market(s)

Real estate buyers and sellers

Industry/Entity Type

Real Estate

Font styles to use
Serif

Colors
000000

Requirements
Must have
• Company name phone number
• Colors: turquoise, white black
Nice to have
• Modern design

```html
<!DOCTYPE html>
<html lang="en">
<head>
<meta charset="UTF-8">
<title>Valtoria Real Estate Services – Available Sign</title>
<link href="https://fonts.googleapis.com/css2?family=Cinzel:wght@600&family=Jost:wght@500&family=Roboto+Condensed:wght@700&display=swap" rel="stylesheet">
<style>
  :root {
    --teal: #1a8d9c;
    --teal-light: #2299a8;
    --teal-dark: #137584;
    --grey-text: #555759;
    --silver-light: #f2f2f2;
    --silver-dark: #8e9396;
    --white: #ffffff;
  }
  * { margin: 0; padding: 0; box-sizing: border-box; }
  html, body {
    width: 900px;
    height: 1200px;
    overflow: hidden;
    background: var(--white);
  }
  .sign {
    position: relative;
    width: 900px;
    height: 1200px;
    background: var(--white);
  }
  .brand-mark {
    position: absolute;
    top: 173px;
    left: 340px;
    width: 220px;
    height: 220px;
    background: var(--teal);
  }
  .brand-name,
  .brand-tagline,
  .sale-text {
    position: absolute;
    left: 0;
    width: 900px;
    text-align: center;
    line-height: 1;
    white-space: nowrap;
  }
  .brand-name {
    top: 545px;
    font-family: "Cinzel", "Times New Roman", serif;
    font-weight: 600;
    font-size: 140px;
    letter-spacing: 2px;
    color: var(--teal);
  }
  .brand-tagline {
    top: 693px;
    font-family: "Jost", "Futura", sans-serif;
    font-weight: 500;
    font-size: 42px;
    letter-spacing: 9px;
    padding-left: 9px;
    color: var(--grey-text);
  }
  .sale-band {
    position: absolute;
    left: 0;
    top: 0;
    width: 900px;
    height: 1200px;
  }
  .sale-text {
    font-family: "Roboto Condensed", "Arial Narrow", sans-serif;
    font-weight: 700;
    color: var(--white);
  }
  .sale-heading {
    top: 897px;
    font-size: 155px;
  }
  .sale-phone {
    top: 1046px;
    font-size: 122px;
  }
</style>
</head>
<body>
  <main class="sign">
    <svg class="sale-band" width="900" height="1200" viewBox="0 0 900 1200" aria-hidden="true">
      <defs>
        <linearGradient id="silverEdge" x1="0" y1="0" x2="1" y2="0">
          <stop offset="0" stop-color="#8e9396"/>
          <stop offset="0.5" stop-color="#f2f2f2"/>
          <stop offset="1" stop-color="#8e9396"/>
        </linearGradient>
        <linearGradient id="tealFill" x1="0" y1="0" x2="0" y2="1">
          <stop offset="0" stop-color="#2299a8"/>
          <stop offset="1" stop-color="#137584"/>
        </linearGradient>
      </defs>
      <path d="M0 943 Q450 635 900 943 L900 955 Q450 647 0 955 Z" fill="url(#silverEdge)"/>
      <path d="M0 958 Q450 650 900 958 L900 1200 L0 1200 Z" fill="url(#tealFill)"/>
    </svg>

    <header class="brand">
      <div class="brand-mark"></div>
      <h1 class="brand-name">VALTORIA</h1>
      <p class="brand-tagline">REAL ESTATE SERVICES</p>
    </header>

    <p class="sale-text sale-heading">AVAILABLE</p>
    <p class="sale-text sale-phone">505-281-7094</p>
  </main>
</body>
</html>
```